Pregnancy and Fertility Information Website

Hello Designers,
I need a website which provide tips and information about healthy and happy pregnancy. My website name is Lorvin medical.

The website should provide all the information needed throughout pregnancy and beyond ranging from pregnancy tracking tools and articles about common pregnancy concerns and what to expect during pregnancy,etc.
The details about first trimester, second trimester and third trimester should be highlighted in the website.

Top Navigation
Home, Fertility, Pregnancy basics, Articles, Tips and News

I'm looking for a simple and clean design which involves captivating images and colors but it shouldn't be crowded. The design must be professional and modern. An easy to navigate layout is a must.

Green, violet, blue and light yellow colors are my favorites but i'm open to other options.

Any questions. Kindly ask

Industry/Entity Type

Medical

```html
<!DOCTYPE html>
<html lang="en">
<head>
<meta charset="utf-8">
<title>Lorvin medical – Pregnancy Tips &amp; Info</title>
<link href="https://fonts.googleapis.com/css2?family=Open+Sans:wght@400;600;700&display=swap" rel="stylesheet">
<style>
:root{
  --violet:#6b2fb8;
  --violet-dark:#5a25a6;
  --text:#6a6a6a;
  --nav-bg:rgba(60,60,60,.45);
  --sidebar-bg:#f4f4f4;
  --white:#ffffff;
  --link-blue:#2ea3f2;
}
*{margin:0;padding:0;box-sizing:border-box}
html,body{width:1200px;height:2521px;overflow:hidden}
body{position:relative;background:var(--white);font-family:"Open Sans",Arial,sans-serif;color:var(--text)}
.hero{position:absolute;left:0;top:0;width:1200px;height:649px;
  background:linear-gradient(100deg,#8d9295 0%,#a9adaf 35%,#c9c6c1 60%,#8f8d89 100%)}
.nav-bar{position:absolute;left:0;top:0;width:1200px;height:67px;background:var(--nav-bg)}
.brand{position:absolute;left:148px;top:0;width:101px;height:100px;background:var(--white);
  clip-path:polygon(0 0,100% 0,100% 82%,50% 100%,0 82%);display:flex;flex-direction:column;align-items:center;justify-content:center;gap:6px}
.brand-dot{width:18px;height:18px;border-radius:50%;background:var(--violet)}
.brand-name{font-size:11px;font-weight:600;color:var(--violet);text-align:center;line-height:1.1}
.main-nav{position:absolute;top:26px;left:647px;display:flex;gap:0}
.main-nav a{position:absolute;white-space:nowrap;font-size:12px;font-weight:700;color:var(--white);text-decoration:none}
.main-nav .current{color:var(--link-blue);font-weight:600}
.search-icon{position:absolute;left:1038px;top:25px}
.hero-title{position:absolute;left:121px;top:288px;font-size:44px;font-weight:400;color:var(--white);letter-spacing:.5px}
.hero-sub{position:absolute;left:121px;top:344px;font-size:18px;font-weight:600;color:var(--white)}
.hero-btn{position:absolute;left:119px;top:383px;width:133px;height:40px;border:2px solid var(--white);
  color:var(--white);font-size:15px;display:flex;align-items:center;justify-content:center;letter-spacing:.5px}
.scroll-down{position:absolute;left:583px;top:592px}
.content{position:absolute;left:84px;top:710px;width:660px}
.section-title{font-size:25px;font-weight:400;color:var(--violet);margin-bottom:44px}
.content p{font-size:13.3px;line-height:19.4px;text-align:justify;margin-bottom:19px}
.stages{display:block;width:524px;height:252px;margin:36px 0 48px 84px;
  background:linear-gradient(180deg,#f7f1f8,#e9d7ec);border-radius:4px}
.stages-title{margin-top:0}
.sidebar{position:absolute;left:826px;top:717px;width:290px;height:1240px;background:var(--sidebar-bg)}
.card{position:absolute;left:11px;width:267px}
.card-photo{width:267px;height:190px;border:4px solid var(--white);box-shadow:0 10px 12px -6px rgba(0,0,0,.35)}
.card h3{font-size:19px;font-weight:400;color:var(--violet);margin-top:62px;margin-bottom:4px}
.card p{font-size:11.5px;line-height:19.5px;width:267px}
.gallery{position:absolute;left:37px;top:2113px}
.footer{position:absolute;left:0;top:2476px;width:1200px;height:45px;background:var(--violet-dark)}
.social{position:absolute;right:235px;top:13px;display:flex;gap:22px}
.social span{width:19px;height:19px;border-radius:50%;background:var(--white)}
</style>
</head>
<body>
<header class="hero" role="img" aria-label="Photo of a pregnant woman holding a cup beside a tall window">
  <div class="nav-bar"></div>
  <div class="brand"><span class="brand-dot"></span><span class="brand-name">Lorvin medical</span></div>
  <nav class="main-nav">
    <a class="current" style="left:0">Home</a>
    <a style="left:55px">Fertility</a>
    <a style="left:121px">Pregnancy Basics</a>
    <a style="left:240px">Articles</a>
    <a style="left:304px">Tips &amp; News</a>
  </nav>
  <svg class="search-icon" width="16" height="16" viewBox="0 0 16 16"><circle cx="6.5" cy="6.5" r="5" fill="none" stroke="#fff" stroke-width="1.6"/><line x1="10" y1="10" x2="15" y2="15" stroke="#fff" stroke-width="1.8"/></svg>
  <h1 class="hero-title">PREGNANCY TIPS &amp; INFO.</h1>
  <div class="hero-sub">Pregnancy Symptoms, Signs of Pregnancy, Baby Care</div>
  <div class="hero-btn">READ MORE</div>
  <svg class="scroll-down" width="36" height="36" viewBox="0 0 36 36"><circle cx="18" cy="18" r="16.5" fill="none" stroke="#fff" stroke-width="2"/><polyline points="11,15 18,22 25,15" fill="none" stroke="#fff" stroke-width="2.4"/></svg>
</header>

<main class="content">
  <h2 class="section-title">Pregnancy Symptoms, Signs of Pregnancy, Baby Care</h2>
  <p>This website as it's names suggests so clearly, strives to provide useful information about various aspects of one of the most wonderful phenomenon of nature: Pregnancy. We gather useful information and advice from various reputable sources about pregnancy and childbirth, starting with planning to conceive, to week by week pregnancy progress, to childbirth, to post-natal care.</p>
  <p>Pregnancy is a very extraordinary time for you as the expectant mother and your partner. Knowing what is happening to you and your growing baby during the weeks ahead will help you both to enjoy this exhilarating period in your life. Starting with pre conceptual care, you get information on how conception takes place and then look at pregnancy and your baby's development week by week. It is normal to experience some minor discomforts during pregnancy and you will want to know how to cope with them. More serious problems can occasionally occur so it is important for you to recognize such symptoms and seek immediate medical help.</p>
  <p>You may be anxious about the birth and hence you are provided with the choices available in childbirth. Being informed you will be able to choose the care and the birth that is right for you.</p>
  <p>As your body adapts to the changes that pregnancy brings, you will begin to prepare yourself physically, emotionally and practically for parenthood. A well-balanced healthy diet is essential for both you and your baby. Exercise has an important part too, not only it keeps you fit but it also helps you to in preparing your body for birth.</p>
  <div class="stages" role="img" aria-label="Illustration of pregnancy stages: first, second and third trimester silhouettes and a mother holding her baby at birth"></div>
  <h2 class="section-title stages-title">Pregnancy</h2>
  <p>The time to plan for a pregnancy is before you happen to be pregnant. Your health and the health of your new baby depend on you. It is also significant to consider that most women do not recognize they are pregnant for three to four weeks and many pregnancies are unanticipated. By the time you discover out you are pregnant your baby is already forming major organs and structures.</p>
  <p>First take 400 mcg of folic acid (a B vitamin) every day to help prevent defects of the brain and spinal cord. It is safe to take a multivitamin. Avoid high doses of vitamins which may be harmful. Iron and calcium are also important your caffeine. Drink no more than two cups of coffee or six glasses of tea or soda per day. Try to reach a healthy weight before you become pregnant. You should not be on a weight-loss diet during pregnancy.</p>
  <p style="margin-top:38px">Smoking cigarettes increases your risk of miscarriage or having a baby with a low birth weight. Alcohol and illegal drugs such as cocaine, marijuana, and heroin can cause birth defects or other problems with your baby.</p>
  <p>You may be anxious about the birth and hence you are provided with the choices available in childbirth. Being informed you will be able to choose the care and the birth that is right for you.</p>
</main>

<aside class="sidebar">
  <article class="card" style="top:9px">
    <div class="card-photo" role="img" aria-label="Photo of a smiling pregnant woman outdoors among autumn trees" style="background:linear-gradient(135deg,#8a6a3e,#c9a36b 55%,#6b5434)"></div>
    <h3>Pregnancy</h3>
    <p>Preparing yourself for labor and devising a birth plan is one of the best ways to get ready for the big day. Get great tips on the birthing process, pain medications, and on what to do if you need a caesarian delivery.</p>
  </article>
  <article class="card" style="top:420px">
    <div class="card-photo" role="img" aria-label="Photo of a pregnant woman resting on a white sofa" style="background:linear-gradient(135deg,#e9e4df,#cfc3b8 55%,#f3efea)"></div>
    <h3>Labor and Birth</h3>
    <p>Preparing yourself for labor and devising a birth plan is one of the best ways to get ready for the big day. Get great tips on the birthing process, pain medications, and on what to do if you need a caesarian delivery.</p>
  </article>
  <article class="card" style="top:830px">
    <div class="card-photo" role="img" aria-label="Photo of an expecting couple standing above a city of red rooftops" style="background:linear-gradient(180deg,#7fa9d6 0%,#a9c6e4 45%,#b07a5a 75%,#8c5e45)"></div>
    <h3>Baby Care</h3>
    <p>Preparing yourself for labor and devising a birth plan is one of the best ways to get ready for the big day. Get great tips on the birthing process, pain medications, and on what to do if you need a caesarian delivery.</p>
  </article>
</aside>

<svg class="gallery" width="1126" height="293" viewBox="0 0 1126 293">
  <defs>
    <linearGradient id="g1" x1="0" x2="1"><stop offset="0" stop-color="#c9a35a"/><stop offset="1" stop-color="#6f86a8"/></linearGradient>
    <linearGradient id="g2" x1="0" x2="1"><stop offset="0" stop-color="#b98a5c"/><stop offset="1" stop-color="#d99a6c"/></linearGradient>
    <linearGradient id="g3" x1="0" x2="1"><stop offset="0" stop-color="#dfe3e6"/><stop offset="1" stop-color="#c8a98a"/></linearGradient>
    <linearGradient id="g4" x1="0" x2="1"><stop offset="0" stop-color="#d9d6d2"/><stop offset="1" stop-color="#c33a3a"/></linearGradient>
  </defs>
  <polygon role="img" aria-label="Photo of a woman choosing products on a pharmacy shelf" points="0,0 272,0 223,293 0,293" fill="url(#g1)"/>
  <polygon role="img" aria-label="Photo of a happy couple sharing food in a kitchen" points="287,0 572,0 523,293 238,293" fill="url(#g2)"/>
  <polygon role="img" aria-label="Photo of a doctor talking with a female patient" points="587,0 887,0 838,293 538,293" fill="url(#g3)"/>
  <polygon role="img" aria-label="Photo of a pregnant woman in red using a laptop" points="902,0 1126,0 1126,293 853,293" fill="url(#g4)"/>
</svg>

<footer class="footer">
  <div class="social"><span></span><span></span><span></span><span></span></div>
</footer>
</body>
</html>
```